Postcard Design for a Church

The postcard is for a church. This will be going to new movers in the area. I would like it to say "Welcome to the Neighborhood!" somewhere on the postcard. You can say something like like "Transitioning to a new community can be very difficult and sometimes overwhelming. Our goal as a church is to assist and help where needed". You can also say something like "if you're looking for a church home and a place where you'll be embraced, we invite you to worship with us and be our special guest". Our Facebook page is Friendwall.com/TheBrightwaterHouseTN. Our Twitter is TheBrightwaterHouse. Our website page is www.TheBrightwaterHouseTN.org. You can list the vision of the church which is "Our vision is to save souls, change lives & impact the community". Please list the address of the church being located in the main auditorium of Marrowfield High School. The time is Sundays at 11am. The address is 1786 Marrowfield Lane, Dunmore, TN 37588. Our colors are purple and gold. You can also say "We're more than a church, we're a family". I would like it to also say something like "Come and Grow With Us!" My name is Pastor Desmond "LT" Fairbanks. My wife's name is First Lady Mirelle Fairbanks. I hope all this makes sense and it's not exactly in order, but I would like to see your designs. Thank you.

```html
<!DOCTYPE html>
<html lang="en">
<head>
<meta charset="utf-8">
<title>The Brightwater House – Welcome Postcard</title>
<link rel="stylesheet" href="https://fonts.googleapis.com/css2?family=Lato:ital,wght@0,400;0,700;0,900;1,400;1,700&display=swap">
<style>
:root{
  --purple:#46245f;
  --purple-deep:#33184a;
  --gold:#c9b57a;
  --gold-light:#e9dca6;
  --gold-dark:#a88f4f;
  --white:#ffffff;
  --ink:#3b1d55;
  --line-grey:#e6e6e6;
  --stage:#2a1a10;
}
*{margin:0;padding:0;box-sizing:border-box}
html,body{width:1000px;height:1200px;overflow:hidden}
body{background:var(--stage);font-family:"Lato",Arial,sans-serif;position:relative}
.card{position:absolute;left:131px;width:750px;height:578px;overflow:hidden}
.card--front{top:14px;background:var(--purple)}
.card--back{top:610px;background:var(--white)}
.card-art{position:absolute;left:0;top:0;width:750px;height:578px}
.logo-box{position:absolute;left:36px;top:0;width:165px;height:208px;background:var(--white);display:flex;flex-direction:column;align-items:center;justify-content:center;gap:12px}
.logo-dot{width:96px;height:96px;border-radius:50%;background:var(--purple)}
.logo-name{color:var(--ink);font-weight:700;font-size:19px;line-height:1.1;text-align:center}
.headline{position:absolute;left:220px;top:34px;width:494px;color:var(--gold-light);font-weight:900;text-transform:uppercase;text-shadow:0 2px 3px rgba(0,0,0,.45)}
.headline .big{font-size:44px;letter-spacing:.5px}
.headline .small{font-size:30px}
.headline .line2{display:block;text-align:right;font-size:42px;margin-top:-4px}
.intro{position:absolute;left:218px;top:144px;width:490px;color:var(--white);font-size:17px;line-height:22px;text-align:justify}
.invite{position:absolute;left:33px;top:225px;width:402px;color:var(--gold-light);font-size:16.5px;line-height:22px}
.vision-label{position:absolute;left:33px;top:305px;color:var(--white);font-style:italic;font-weight:700;font-size:14px;display:flex;align-items:center;gap:10px}
.vision-label .mark{width:12px;height:12px;border-radius:50%;background:var(--white)}
.vision-text{position:absolute;left:33px;top:332px;color:var(--white);font-style:italic;font-size:13.5px;letter-spacing:.2px}
.dots{position:absolute;height:0;border-top:3px dotted var(--gold)}
.front-dots{left:33px;top:364px;width:372px}
.address{position:absolute;left:33px;top:380px;color:var(--gold-light);font-size:16px;line-height:22px;font-style:normal}
.address strong{font-weight:700}
.service-time{position:absolute;left:262px;top:446px;color:var(--white);font-size:16px}
.grow{position:absolute;left:32px;top:507px;color:var(--ink);font-weight:900;font-size:24px}
.pastors{position:absolute;left:32px;top:541px;color:#222;font-size:14px}
.back-tagline{position:absolute;left:29px;top:40px;color:var(--gold);font-weight:700;text-transform:uppercase;font-size:24px;line-height:36px}
.back-tagline .lg{font-size:28px}
.back-dots-1{left:26px;top:173px;width:296px}
.back-dots-2{left:26px;top:294px;width:240px}
.social{position:absolute;left:29px;list-style:none;color:var(--white);font-size:14px;display:flex;align-items:center;gap:11px}
.social .icon{width:18px;height:18px;border-radius:50%;background:var(--white)}
.social--one{top:208px}
.social--two{top:242px}
.web{position:absolute;left:29px;top:321px;color:var(--gold);font-size:15px}
.back-logo{position:absolute;left:10px;top:446px;display:flex;flex-direction:column;align-items:center;gap:6px;width:90px}
.back-logo .logo-dot{width:70px;height:70px;border:3px solid var(--gold)}
.back-logo .logo-name{font-size:11px;white-space:nowrap}
.stamp{position:absolute;left:589px;top:28px;width:137px;height:142px;border:4px solid var(--line-grey)}
.addr-line{position:absolute;left:401px;width:326px;height:4px;background:var(--line-grey)}
.addr-line--1{top:275px}
.addr-line--2{top:337px}
.addr-line--3{top:400px}
.addr-line--4{top:469px}
</style>
</head>
<body>

<section class="card card--front" aria-label="Postcard front">
  <svg class="card-art" viewBox="0 0 750 578" aria-hidden="true">
    <rect x="0" y="486" width="750" height="92" fill="#ffffff"/>
    <line x1="0" y1="485" x2="440" y2="485" stroke="#c9b57a" stroke-width="6"/>
    <circle cx="652" cy="432" r="222" fill="#c9b57a"/>
  </svg>
  <svg class="card-art" viewBox="0 0 750 578" role="img" aria-label="Photo of the pastor and his wife standing together, smiling">
    <defs>
      <linearGradient id="photoTone" x1="0" y1="0" x2="1" y2="1">
        <stop offset="0" stop-color="#e7e4df"/>
        <stop offset=".55" stop-color="#8a7a70"/>
        <stop offset="1" stop-color="#1e1a1c"/>
      </linearGradient>
    </defs>
    <circle cx="652" cy="432" r="214" fill="url(#photoTone)"/>
  </svg>

  <div class="logo-box">
    <div class="logo-dot"></div>
    <div class="logo-name">The Brightwater House</div>
  </div>

  <h1 class="headline">
    <span class="big">Welcome</span> <span class="small">to the</span>
    <span class="line2">Neighborhood!</span>
  </h1>

  <p class="intro">Transitioning to a new community can be very difficult and sometimes overwhelming. Our goal as a church is to assist and help where needed.</p>

  <p class="invite">If you're looking for a church home and a place where you'll be embraced, we invite you to worship with us and be our special guest.</p>

  <p class="vision-label"><span class="mark"></span>OUR VISION IS TO:</p>
  <p class="vision-text">SAVE SOULS, CHANGE LIVES, IMPACT THE COMMUNITY</p>

  <div class="dots front-dots"></div>

  <address class="address">
    Address:<br>
    <strong>Marrowfield High School</strong> (main auditorium)<br>
    1786 Marrowfield Lane,<br>
    Dunmore, TN 37588
  </address>
  <p class="service-time">Sundays at 11am</p>

  <h2 class="grow">COME AND GROW WITH US!</h2>
  <p class="pastors">Pastor Desmond "LT" Fairbanks &amp; wife Lady Mirelle Fairbanks</p>
</section>

<section class="card card--back" aria-label="Postcard back">
  <svg class="card-art" viewBox="0 0 750 578" aria-hidden="true">
    <path d="M0 578 C 150 540, 300 460, 345 300 C 330 420, 250 520, 120 578 Z" fill="#eeeeee"/>
    <path d="M140 578 C 260 530, 340 450, 360 330 C 352 440, 300 520, 230 578 Z" fill="#f3f3f3"/>
    <ellipse cx="100" cy="200" rx="262" ry="238" fill="#d8cc98"/>
    <ellipse cx="94" cy="198" rx="254" ry="232" fill="#46245f"/>
  </svg>

  <h2 class="back-tagline">We're more than<br><span class="lg">a church,</span><br><span class="lg">we're a family</span></h2>

  <div class="dots back-dots-1"></div>
  <ul>
    <li class="social social--one"><span class="icon"></span>www.friendwall.com/TheBrightwaterHouseTN</li>
    <li class="social social--two"><span class="icon"></span>www.chirpline.com/TheBrightwaterHouse</li>
  </ul>
  <div class="dots back-dots-2"></div>
  <p class="web">www.TheBrightwaterHouseTN.org</p>

  <div class="back-logo">
    <div class="logo-dot"></div>
    <div class="logo-name">The Brightwater House</div>
  </div>

  <div class="stamp"></div>
  <div class="addr-line addr-line--1"></div>
  <div class="addr-line addr-line--2"></div>
  <div class="addr-line addr-line--3"></div>
  <div class="addr-line addr-line--4"></div>
</section>

</body>
</html>
```